Fresh Fern Home Care Co Chemical Free need Web site

need web site that is simple yet informative and I am able to post articles under that heading, a blog drop down menu I want to also have a Membership area, where visitors are promoted to join to know the real secrets of The Green Horizon Papers and Notes about our real world. Fee $ 77.00 a year, which automatically adds their details to my data base collected when they first try to interact on the site (pop up window) If I cant generate traffic and some customers by Thursday I will have to leave town... I really don't have a clue but it has to be educational but user friendly and interactive as well. The I also need to know how it is that I add thing into there as well. Am willing to negotiate price if someone creates a beauty, try hard guys I need help and fast. Lots of generated traffic and mobile app friendly, book cleaning via apps, and have a virtual receptionist. No missed calls allowed...

NOTE: If the design of the website is inclusive of all the features one would have in a complete package I am willing to pay $1000.00, Its got to be a knock out. It must be easy for me to post articles under drop down bars, areas of interest, look at the pictures for inspiration about chemical exposure and residue left after cleaning etc, need daily update on a blog page, content creator, so ranking are higher in search engines. I am sure you know what I want, the whole deal, packaged up looking very informative, promoting the business fresh fern home care co, v's chemical exposure constantly, get facts etc.

I am willin gto pay for the complete package to reduce the time I have to spend, creating content and posting new articles, I only will go on there when business goes quiet and then promote to all email addresses a deal of the week.. type thing.

It must have a blog and back links bla bla, a area for others to buy ad space and pay me, broadcast to all the social site known so far, a members are, facility to pay this, cash kite? have an app for mobile friendly, for when someone wants to schedule time to clean. I need to gain all the possible information before even entering the website itself, just a nice pop up, request name and email and contact; for use of mass txt alerts.

                                   

Good luck I hope that a good incentive for you all.

```html
<!DOCTYPE html>
<html lang="en">
<head>
<meta charset="utf-8">
<title>Clearwave Cleaning Solutions</title>
<link rel="stylesheet" href="https://fonts.googleapis.com/css2?family=Open+Sans:wght@400;600&family=Oswald:wght@300;400&family=Quicksand:wght@500;600&display=swap">
<style>
:root{
  --brand:#3b3f9f;
  --brand-dark:#2f3388;
  --ink:#333;
  --muted:#777;
  --night:#000;
  --accent-blue:#1d7cc2;
  --rule-red:#e08a8a;
  --tick-red:#c8202a;
  --card-bg:#fafafa;
  --white:#fff;
}
*{box-sizing:border-box;margin:0;padding:0}
html,body{width:938px;height:1200px;overflow:hidden;background:var(--white)}
body{position:relative;font-family:"Open Sans",sans-serif;color:var(--ink)}
.abs{position:absolute}

.topbar{left:0;top:0;width:938px;height:35px;background:var(--brand);color:var(--white)}
.topbar .phone{left:135px;top:9px;font-size:12px}
.topbar .follow{left:660px;top:10px;font-size:11px;font-weight:600}
.topbar svg{position:absolute;left:729px;top:6px}

.header{left:0;top:35px;width:938px;height:387px;background:var(--night)}
.logo-mark{left:160px;top:68px;width:32px;height:32px;border-radius:50%;background:var(--brand)}
.logo-name{left:227px;top:60px;font-family:"Oswald",sans-serif;font-weight:300;color:#e8e8e8;font-size:18px;line-height:27px;letter-spacing:-.2px}
.nav{left:472px;top:74px;display:flex;gap:20px;font-family:"Quicksand",sans-serif;font-weight:600;font-size:11px;color:var(--white);letter-spacing:.2px}
.nav .current{position:relative}
.nav .current::after{content:"";position:absolute;left:0;top:20px;width:32px;height:3px;background:var(--brand)}

.slider{left:135px;top:132px;width:670px;height:354px;background:var(--white);box-shadow:0 6px 8px rgba(0,0,0,.12)}
.slider .stage{position:absolute;left:6px;top:6px;width:658px;height:342px;background:var(--night)}
.hero-photo{left:172px;top:178px;width:276px;height:274px;background:linear-gradient(160deg,#14264f 0%,#2b4d8c 50%,#0d1a3a 100%)}
.slide-title{left:489px;top:191px;font-family:"Oswald",sans-serif;font-weight:400;color:var(--white);font-size:28px;line-height:39px;letter-spacing:-1px}
.slide-text{left:492px;top:279px;width:270px;color:var(--white);font-size:9.6px;line-height:16px}
.btn-join{left:492px;top:356px;width:80px;height:29px;background:var(--brand);color:var(--white);font-family:"Quicksand",sans-serif;font-weight:600;font-size:10px;display:flex;align-items:center;justify-content:center;border-radius:2px}
.pager{left:494px;top:404px;display:flex}
.pager span{width:22px;height:22px;display:flex;align-items:center;justify-content:center}
.pager .prev{background:var(--brand)}
.pager .next{background:#3a3a3a}

.welcome{left:0;top:506px;width:938px;text-align:center;font-family:"Quicksand",sans-serif;font-weight:500;font-size:21px;color:#333}
.welcome b{font-weight:500;color:var(--accent-blue)}
.intro{left:120px;top:544px;width:698px;text-align:center;font-size:8.4px;line-height:16px;color:var(--muted)}

.card{top:616px;width:208px;height:254px;background:var(--card-bg);box-shadow:0 3px 4px rgba(0,0,0,.1);text-align:center}
.card .photo{height:134px;border-bottom:2px solid var(--rule-red)}
.card h3{margin-top:15px;font-family:"Quicksand",sans-serif;font-weight:500;font-size:13.5px;color:#333}
.card p{margin:9px 16px 0;font-size:7.8px;line-height:16px;color:var(--muted)}
.card .more{display:block;margin-top:6px;font-family:"Quicksand",sans-serif;font-weight:600;font-size:8.5px;color:var(--brand-dark)}
.photo.people{background:linear-gradient(160deg,#e9e4dd,#3d3a3a 70%,#1b1b1f)}
.photo.wind{background:linear-gradient(180deg,#d8ecec 0%,#9bc7b0 45%,#5f8a2f 75%,#2f4a14)}
.photo.molecule{background:linear-gradient(160deg,#8fd4ef,#2a87b8 55%,#0e4c78)}

.benefits-title{left:133px;top:893px;font-family:"Quicksand",sans-serif;font-weight:500;font-size:24px;color:#333}
.benefits-title b{font-weight:600;color:var(--brand)}
.benefits-text{left:135px;top:937px;width:362px;font-size:8.8px;line-height:16px;color:var(--muted)}
.benefits-list{left:135px;top:1000px;list-style:none;font-size:9.4px;color:#444}
.benefits-list li{height:18.2px;display:flex;align-items:center;gap:9px}
.device{left:518px;top:917px;width:286px;height:177px;border-radius:12px;border:2px solid #bbb;background:linear-gradient(150deg,#0a0a0a 0%,#162a52 50%,#050505 100%)}

.footer{left:0;top:1127px;width:938px;height:73px;background:var(--brand);color:var(--white)}
.footer .links{left:125px;top:19px;font-size:9.6px}
.footer .copy{left:125px;top:44px;font-size:9.6px}
.footer svg{position:absolute;left:667px;top:27px}
</style>
</head>
<body>

<div class="abs topbar">
  <div class="abs phone">Toll Free : +1 - 555 - 014 - 277</div>
  <div class="abs follow">Follow us :</div>
  <svg width="76" height="22" viewBox="0 0 76 22" aria-label="Social links">
    <g fill="none" stroke="#fff" stroke-width="1">
      <circle cx="11" cy="11" r="10"/><circle cx="38" cy="11" r="10"/><circle cx="65" cy="11" r="10"/>
    </g>
  </svg>
</div>

<div class="abs header"></div>
<div class="abs logo-mark"></div>
<div class="abs logo-name">CLEARWAVE CLEANING<br>SOLUTIONS</div>
<nav class="abs nav">
  <span class="current">HOME</span><span>ABOUT</span><span>MEMBERSHIP</span><span>LOCATIONS</span><span>CONTACT</span>
</nav>

<section class="abs slider">
  <div class="stage"></div>
</section>
<div class="abs hero-photo" role="img" aria-label="Photo of planet Earth seen from space"></div>
<h1 class="abs slide-title">YOUR PLANET IS CHANGING.<br>WE'RE ON IT</h1>
<p class="abs slide-text">Lorem ipsum dolor sit amet, consectetur adipiscing elit, sed do eiusmod tempor incididunt ut labore et dolore magna aliqua. Ut enim ad minim veniam, quis nostrud exercitation ullamco laboris nisi ut aliquip ex ea commodo</p>
<div class="abs btn-join">JOIN NOW</div>
<div class="abs pager">
  <span class="prev"><svg width="8" height="8" viewBox="0 0 8 8"><path d="M5.5 1 2.5 4l3 3" fill="none" stroke="#fff" stroke-width="1.4"/></svg></span>
  <span class="next"><svg width="8" height="8" viewBox="0 0 8 8"><path d="M2.5 1l3 3-3 3" fill="none" stroke="#fff" stroke-width="1.4"/></svg></span>
</div>

<h2 class="abs welcome">Welcome To <b>Clearwave Cleaning Solutions</b></h2>
<p class="abs intro">Lorem ipsum dolor sit amet, consectetuer adipiscing elit, sed diam nonummy nibh euismod tincidunt ut laoreet dolore magna aliquam erat volutpat.<br>Ut wisi enim ad minim veniam, quis nostrud exerci tation ullamcorper suscipit lobortis nisl ut aliquip ex ea commodo consequat. Lorem ipsum dolor sit amet,<br>sectetuer adipiscing elit, sed diam nonummy nibh euismod tincidunt ut laoreet dolore magna aliquam erat volutpat.</p>

<article class="abs card" style="left:135px">
  <div class="photo people" role="img" aria-label="Photo of a business audience seated at a seminar"></div>
  <h3>Membership Area</h3>
  <p>Lorem ipsum dolor sit amet, consectetur adip elit, sed do eiusmod tempor incididunt ut labore et dolore magna aliqua.</p>
  <span class="more">Learn More +</span>
</article>
<article class="abs card" style="left:366px">
  <div class="photo wind" role="img" aria-label="Photo of wind turbines on green fields"></div>
  <h3>Sed ut perspiciatis unde</h3>
  <p>Lorem ipsum dolor sit amet, consectetur adip elit, sed do eiusmod tempor incididunt ut labore et dolore magna aliqua.</p>
  <span class="more">Learn More +</span>
</article>
<article class="abs card" style="left:597px">
  <div class="photo molecule" role="img" aria-label="Image of a blue molecular structure"></div>
  <h3>Sed ut perspiciatis unde</h3>
  <p>Lorem ipsum dolor sit amet, consectetur adip elit, sed do eiusmod tempor incididunt ut labore et dolore magna aliqua.</p>
  <span class="more">Learn More +</span>
</article>

<h2 class="abs benefits-title">Your <b>BENEFITS</b></h2>
<p class="abs benefits-text">Lorem ipsum dolor sit amet, consectetur adipiscing elit, sed do eiusmod tempor incididu ut labore et dolore magna aliqua. Ut enim ad minim veniam, quis nostrud exercitation ullamco laboris nisi ut aliquip ex ea commodo consequat. Duis aute irure dolor</p>
<ul class="abs benefits-list">
  <li><svg width="11" height="9" viewBox="0 0 11 9"><path d="M1 5l3 3 6-7" fill="none" stroke="var(--tick-red)" stroke-width="1.8"/></svg>Pretty light of the Moon</li>
  <li><svg width="11" height="9" viewBox="0 0 11 9"><path d="M1 5l3 3 6-7" fill="none" stroke="var(--tick-red)" stroke-width="1.8"/></svg>Science and Space</li>
  <li><svg width="11" height="9" viewBox="0 0 11 9"><path d="M1 5l3 3 6-7" fill="none" stroke="var(--tick-red)" stroke-width="1.8"/></svg>Protect 500 pieces of debris</li>
  <li><svg width="11" height="9" viewBox="0 0 11 9"><path d="M1 5l3 3 6-7" fill="none" stroke="var(--tick-red)" stroke-width="1.8"/></svg>Sunrise over Earth</li>
  <li><svg width="11" height="9" viewBox="0 0 11 9"><path d="M1 5l3 3 6-7" fill="none" stroke="var(--tick-red)" stroke-width="1.8"/></svg>By the light of the Moon</li>
</ul>
<div class="abs device" role="img" aria-label="Photo of a tablet showing Earth from space"></div>

<footer class="abs footer">
  <div class="abs links">Home &nbsp;/&nbsp; About Us &nbsp;/&nbsp; Blogs &nbsp;/&nbsp; Services &nbsp;/&nbsp; User login &nbsp;/&nbsp; Get in Touch</div>
  <div class="abs copy">©2013 - 2014 &nbsp;Clearwave Cleaning Solutions, All Rights Reserved.</div>
  <svg width="130" height="24" viewBox="0 0 130 24" aria-label="Social links">
    <g fill="none" stroke="#fff" stroke-width="1">
      <circle cx="12" cy="12" r="11"/><circle cx="38.5" cy="12" r="11"/><circle cx="65" cy="12" r="11"/><circle cx="91.5" cy="12" r="11"/><circle cx="118" cy="12" r="11"/>
    </g>
  </svg>
</footer>

</body>
</html>
```